Varga Lillas Physiotherapy Business Card Vienna

We need a business card design for a newly created Physiotherapy company based in Vienna Austria.
We seek a simple, modern, minimalist design without too much color variation. The font should look young/fresh, but definitely not childish or so. Since we are a starting Business, we currently haven't got a logo, if you feel like a logo would fit your design, feel free to use one, but it's not necessary.
Target Market(s)
Healthcare, young and elderly people with mobility issues
Industry/Entity Type
Health And Wellness
Contact Information for Business Card
Name: Lilla Varga
Title description: Physiotherapist
Phone num: +43 664 5290 4816
e-mail: lilla.praxis@brelomail.com
Colors
Designer to choose colors to be used in the design.
Requirements
Must have
- Final design language must be in German, basically, the Title Description needs to be "Physiotherapeutin" the other details remain as in the English Language.
Nice to have
- Simple, modern, minimalist design
Should not have
- too many colors, Obvious use of a skeleton, skull, spline

```html
<!DOCTYPE html>
<html lang="de">
<head>
<meta charset="utf-8">
<title>Lilla Varga – Physiotherapeutin</title>
<link href="https://fonts.googleapis.com/css2?family=Red+Hat+Display:wght@400;500;700;800&display=swap" rel="stylesheet">
<style>
  :root {
    --backdrop: #fdfa00;
    --card: #282636;
    --ink: #ffffff;
    --placeholder: #4a4858;
  }
  html, body {
    margin: 0;
    width: 1200px;
    height: 1200px;
    overflow: hidden;
    background: var(--backdrop);
  }
  .card {
    position: absolute;
    left: 100px;
    top: 310px;
    width: 1000px;
    height: 580px;
    background: var(--card);
    font-family: "Red Hat Display", sans-serif;
    color: var(--ink);
  }
  .frame {
    position: absolute;
    left: 100px;
    top: 80px;
    width: 800px;
    height: 380px;
    border: 3px solid var(--ink);
    box-sizing: border-box;
  }
  .name {
    position: absolute;
    right: 130px;
    top: 118px;
    margin: 0;
    font-size: 56px;
    font-weight: 800;
    letter-spacing: 0.5px;
    line-height: 1;
    white-space: nowrap;
  }
  .title {
    position: absolute;
    right: 126px;
    top: 188px;
    margin: 0;
    font-size: 17px;
    font-weight: 400;
    letter-spacing: 9px;
    line-height: 1;
    white-space: nowrap;
  }
  .barbell-placeholder {
    position: absolute;
    left: 118px;
    top: 222px;
    width: 764px;
    height: 56px;
    background: linear-gradient(90deg, var(--placeholder), #3a3848 50%, var(--placeholder));
  }
  .contact {
    position: absolute;
    left: 122px;
    top: 300px;
    margin: 0;
    padding: 0;
    list-style: none;
    font-size: 21px;
    font-weight: 500;
  }
  .contact li {
    display: flex;
    align-items: center;
    gap: 16px;
    height: 44px;
    white-space: nowrap;
  }
  .contact svg { width: 24px; height: 24px; flex: none; }
</style>
</head>
<body>
  <div class="card">
    <div class="frame"></div>
    <h1 class="name">LILLA VARGA</h1>
    <p class="title">PHYSIOTHERAPEUTIN</p>

    <div class="barbell-placeholder" role="img" aria-label="Illustration of a barbell spanning the card"></div>

    <ul class="contact">
      <li>
        <svg viewBox="0 0 24 24" aria-hidden="true"><path fill="#ffffff" d="M6.6 10.8a15.1 15.1 0 0 0 6.6 6.6l2.2-2.2a1 1 0 0 1 1-.25 11.4 11.4 0 0 0 3.6.57 1 1 0 0 1 1 1V20a1 1 0 0 1-1 1A17 17 0 0 1 3 4a1 1 0 0 1 1-1h3.5a1 1 0 0 1 1 1c0 1.25.2 2.45.57 3.57a1 1 0 0 1-.25 1z"/></svg>
        <span>(+43) 664 5290 4816</span>
      </li>
      <li>
        <svg viewBox="0 0 24 24" aria-hidden="true"><path fill="#ffffff" d="M2 5h20v14H2z"/><path fill="none" stroke="#282636" stroke-width="2" d="M2 5l10 8 10-8"/></svg>
        <span>lilla.praxis@brelomail.com</span>
      </li>
    </ul>
  </div>
</body>
</html>
```